Web Design Project (uncoded)

About Us
ZipRoam is a telecom startup and is looking to launch its website.
ZipRoam specializes in providing communication solutions to the travel market. Our mission is to develop cost effective communication products and solutions for the international traveler.
Our simple vision of "every hotel should have a mobile phone in the guest rooms", led us to develop a pathbreaking & cost effective mobile phone. With full integration capabilities with the hotels property management system, location based marketing, user locator and other features, this product is unique in addressing the hospitality segment.
The website is targeted at hotel owners and property management companies.
The website should have a young contemporary and a funky look, in line with the name.
Please find attached our logo (for the colors etc.). (attached now).
We would like to receive the design for a home page and an inside page for the website.
Site map would be as follows: Home, About Us, Solutions, Contact us
Thanks and look forward,
Tomas
Target Market(s)
Hotel decision makers
Industry/Entity Type
Property Management
Look and feel
Each slider illustrates characteristics of the customer's brand and the style your logo design should communicate.

```html
<!DOCTYPE html>
<html lang="en">
<head>
<meta charset="utf-8">
<title>ZipRoam</title>
<link rel="stylesheet" href="https://fonts.googleapis.com/css2?family=Arimo:wght@400;700&family=Lora:ital,wght@1,700&display=swap">
<style>
  :root{
    --orange:#f7941d;
    --orange-light:#fbb040;
    --black:#000;
    --white:#fff;
    --ink:#000;
    --rule:#9a9a9a;
    --pool-a:#6f6fc4;
    --pool-b:#2f9fe0;
  }
  *{box-sizing:border-box;margin:0;padding:0}
  html,body{width:950px;height:1200px;overflow:hidden;background:var(--white)}
  body{position:relative;font-family:"Arimo",Arial,sans-serif;color:var(--ink)}
  .abs{position:absolute}

  /* header */
  .brand{left:14px;top:4px;display:flex;align-items:center;gap:10px}
  .brand-dot{width:80px;height:80px;border-radius:50%;background:var(--orange)}
  .brand-name{font-size:44px;font-weight:700;color:var(--black);letter-spacing:-1px}
  .phone{right:18px;top:33px;display:flex;align-items:center;gap:4px;font-size:15px;color:var(--black)}

  /* nav */
  .nav-band{left:0;top:88px;width:950px;height:45px;background:var(--black)}
  .nav{right:29px;top:93px;display:flex;gap:13px;list-style:none}
  .nav a{display:block;width:128px;height:34px;line-height:33px;text-align:center;color:var(--white);text-decoration:none;font-size:14px;
    background:linear-gradient(160deg,var(--orange-light) 0 45%,var(--orange) 46%);border:1px solid var(--orange-light)}
  .nav a.is-current{background:linear-gradient(90deg,#555,#111);border:2px solid var(--orange);line-height:31px}
  .nav-rule{left:0;top:135px;width:950px;height:5px;background:#e6e6e6}

  /* hero */
  .hero{left:0;top:140px;width:950px;height:333px;background:linear-gradient(100deg,var(--pool-a) 0%,#c7a3b8 45%,#d9a884 60%,var(--pool-b) 100%)}
  .hero-veil{left:0;top:0;width:467px;height:333px;background:rgba(60,60,160,.35)}
  .hero-title{left:47px;top:104px;font-family:"Lora",Georgia,serif;font-style:italic;font-weight:700;font-size:28px;color:var(--orange)}
  .services{left:28px;top:152px;list-style:none}
  .services li{position:relative;padding-left:17px;height:33.5px;font-size:14px;color:var(--orange);display:flex;align-items:center;gap:8px}
  .services li::before{content:"";position:absolute;left:0;top:12px;width:9px;height:9px;border-radius:50%;background:var(--orange)}
  .slider-dots{right:44px;top:316px;display:flex;gap:3px}
  .slider-dots span{width:12px;height:12px;border-radius:50%;background:var(--orange)}
  .slider-dots span.is-active{width:14px;height:14px;border:2px solid var(--black);margin-top:-1px}
  .hero-shadow{left:60px;top:476px;width:830px;height:34px;border-radius:50%;background:radial-gradient(ellipse at center top,rgba(0,0,0,.35),rgba(0,0,0,0) 70%)}

  /* cards */
  .card{top:520px;width:430px}
  .card-head{height:40px;border-radius:5px 5px 0 0;background:linear-gradient(var(--orange-light),var(--orange));color:var(--white);font-weight:700;font-size:18px;line-height:40px;padding-left:20px}
  .card-body{margin-top:1px;height:334px;border:1px solid var(--black);padding:5px 3px;font-size:11px;line-height:13.3px;box-shadow:0 1px 3px rgba(0,0,0,.3)}
  .card-top{display:flex;justify-content:space-between;min-height:200px}
  .card-lead{width:206px;padding:8px 0 0 2px}
  .card-photo{width:213px;height:198px;flex:none}
  .card-more{display:block;text-align:right;padding-right:76px;margin-top:5px;color:var(--orange);text-decoration:underline}

  /* footer */
  .footer{left:0;top:968px;width:950px;height:232px;background:var(--black);color:var(--white)}
  .footer-nav{left:19px;top:12px;list-style:none;display:flex;font-size:14px}
  .footer-nav li:nth-child(1){width:133px}
  .footer-nav li:nth-child(2){width:129px}
  .footer-nav li:nth-child(3){width:147px}
  .footer-rule{left:0;top:92px;width:950px;height:1px;background:var(--rule)}
  .footer-note{left:102px;top:128px;width:750px;font-size:8px;line-height:9.5px}
  .footer-rule-short{left:97px;top:184px;width:752px;height:1px;background:var(--rule)}
  .copyright{left:0;top:221px;width:977px;text-align:center;font-size:8px}
</style>
</head>
<body>

<header>
  <div class="abs brand"><span class="brand-dot"></span><span class="brand-name">ZipRoam</span></div>
  <div class="abs phone">
    <svg width="18" height="18" viewBox="0 0 24 24" aria-hidden="true"><path d="M6.6 10.8a15.2 15.2 0 0 0 6.6 6.6l2.2-2.2c.3-.3.7-.4 1-.2 1.1.4 2.3.6 3.6.6.6 0 1 .4 1 1V20c0 .6-.4 1-1 1A17 17 0 0 1 3 4c0-.6.4-1 1-1h3.5c.6 0 1 .4 1 1 0 1.3.2 2.5.6 3.6.1.3 0 .7-.2 1z" fill="#222"/></svg>
    0(47)55501890
  </div>
</header>

<nav>
  <div class="abs nav-band"></div>
  <ul class="abs nav">
    <li><a class="is-current" href="#">Home</a></li>
    <li><a href="#">About us</a></li>
    <li><a href="#">Our solutions</a></li>
    <li><a href="#">Contact us</a></li>
  </ul>
  <div class="abs nav-rule"></div>
</nav>

<section class="abs hero" role="img" aria-label="Photo of a hotel building with a lit swimming pool at dusk">
  <div class="abs hero-veil"></div>
  <h2 class="abs hero-title">Services</h2>
  <ul class="abs services">
    <li>is simply dummy text of the printing and typesetting industry <svg width="22" height="20" viewBox="0 0 22 20" aria-hidden="true"><circle cx="9" cy="11" r="7.5" fill="none" stroke="var(--orange)" stroke-width="3"/><path d="M6 10l3 4 8-12" fill="none" stroke="#000" stroke-width="3"/></svg></li>
    <li>Lorem Ipsum has been the industry's standard dummy <svg width="22" height="20" viewBox="0 0 22 20" aria-hidden="true"><circle cx="9" cy="11" r="7.5" fill="none" stroke="var(--orange)" stroke-width="3"/><path d="M6 10l3 4 8-12" fill="none" stroke="#000" stroke-width="3"/></svg></li>
    <li>Lorem Ipsum is not simply random text <svg width="22" height="20" viewBox="0 0 22 20" aria-hidden="true"><circle cx="9" cy="11" r="7.5" fill="none" stroke="var(--orange)" stroke-width="3"/><path d="M6 10l3 4 8-12" fill="none" stroke="#000" stroke-width="3"/></svg></li>
    <li>a Latin professor at Harrow Vale College in Virginia <svg width="22" height="20" viewBox="0 0 22 20" aria-hidden="true"><circle cx="9" cy="11" r="7.5" fill="none" stroke="var(--orange)" stroke-width="3"/><path d="M6 10l3 4 8-12" fill="none" stroke="#000" stroke-width="3"/></svg></li>
    <li>but the majority have suffered alteration in some form <svg width="22" height="20" viewBox="0 0 22 20" aria-hidden="true"><circle cx="9" cy="11" r="7.5" fill="none" stroke="var(--orange)" stroke-width="3"/><path d="M6 10l3 4 8-12" fill="none" stroke="#000" stroke-width="3"/></svg></li>
  </ul>
  <div class="abs slider-dots"><span class="is-active"></span><span></span><span></span><span></span></div>
</section>
<div class="abs hero-shadow"></div>

<main>
  <article class="abs card" style="left:8px">
    <h3 class="card-head">About dummy text Lorem Ipsum</h3>
    <div class="card-body">
      <div class="card-top">
        <p class="card-lead">random text. It has roots in a piece of classical Latin literature from 45 BC, making it over 2000 years old. Elias Marwood, a Latin professor at Harrow Vale College in Virginia, looked up one of the more obscure Latin words, consectetur, from a Lorem Ipsum passage, and going through the cites of the word in classical literature, ered the undoubtable source. Lorem Ipsum comes from sections 1.10.32 and 1.10.33 of "de Finibus Bonorum et Malorum" (The , comes from a line in section 1.10.32.</p>
        <div class="card-photo" role="img" aria-label="Photo of a bright living room with a sofa and framed prints" style="background:linear-gradient(160deg,#e8e4dc,#b9a48c 60%,#7a3b20)"></div>
      </div>
      <p>Contrary to popular belief, Lorem Ipsum is not simply random text. It has roots in a piece of classical Latin literature from 45 BC, making it over 2000 years old. Elias Marwood, a Latin professor at Harrow Vale College in Virginia, looked up one of the more obscure Latin words, consectetur, from a Lorem Ipsum passage, and going through the cites of the word in classical literature, discovered the undoubtable source. Lorem Ipsum comes from sections 1.10.32 and 1.10.33 of "de Finibus Bonorum et Malorum" (The , comes from a line in section 1.10.32.</p>
      <a class="card-more" href="#">See more &gt;</a>
    </div>
  </article>

  <article class="abs card" style="left:511px">
    <h3 class="card-head">About dummy text Lorem Ipsum</h3>
    <div class="card-body">
      <div class="card-top">
        <p class="card-lead">random text. It has roots in a piece of classical Latin literature from 45 BC, making it over 2000 years old. Elias Marwood, a Latin professor at Harrow Vale College in Virginia, looked up one of the more obscure Latin words, consectetur, from a Lorem Ipsum passage, and going through the cites of the word in classical literature, ered the undoubtable source. Lorem Ipsum comes from sections 1.10.32 and 1.10.33 of "de Finibus Bonorum et Malorum" (The , comes from a line in section 1.10.32.</p>
        <div class="card-photo" role="img" aria-label="Photo of a living room with cream armchairs and a wooden cabinet" style="background:linear-gradient(160deg,#d9cfc2,#a0684a 55%,#efe6da)"></div>
      </div>
      <p>Contrary to popular belief, Lorem Ipsum is not simply random text. It has roots in a piece of classical Latin literature from 45 BC, making it over 2000 years old. Elias Marwood, a Latin professor at Harrow Vale College in Virginia, looked up one of the more obscure Latin words, consectetur, from a Lorem Ipsum passage, and going through the cites of the word in classical literature, discovered the undoubtable source. Lorem Ipsum comes from sections 1.10.32 and 1.10.33 of "de Finibus Bonorum et Malorum" (The , comes from a line in section 1.10.32.</p>
      <a class="card-more" href="#">See more &gt;</a>
    </div>
  </article>
</main>

<footer class="abs footer">
  <ul class="abs footer-nav">
    <li>Home</li><li>About us</li><li>Our solutions</li><li>Contact us</li>
  </ul>
  <div class="abs footer-rule"></div>
  <p class="abs footer-note">There are many variations of passages of Lorem Ipsum available, but the majority have suffered alteration in some form, by injected humour, or randomised words which don't look even slightly believable. If you are going to use a passage of Lorem Ipsum, you need to be sure there isn't anything embarrassing hidden in the middle of text. All the Lorem Ipsum generators on the Internet tend to repeat predefined chunks as necessary, making this the first true generator on the Internet. It uses a dictionary of over 200 Latin words, combined with a handful of model sentence structures, to generate Lorem Ipsum which looks reasonable. The generated Lorem Ipsum is therefore always free from repetition, injected humour, or non-characteristic words etc.</p>
  <div class="abs footer-rule-short"></div>
  <p class="abs copyright">Copyright 1992 to 2013 all rights reserved</p>
</footer>

</body>
</html>
```